Business Card Design

Business card design and logo for new company called PRT Holdings, Inc.
No specific business product line so design would be more focused on the Company name and type style. I would like logo to incorporate Company Lettering "PRT" . Classic example of that would be the Vex Broadcasting logo. Intent that the "PRT" lettering design would also be the Company Logo design.
Note that contact information for business card does not have telephone / fax numbers and web site as that will follow but make allowance for that information in the business card design. Several of the design layouts has small logo instead of the wording for phone, fax ..... which I would prefer.
Target Market(s)
Small Businesses
Industry/Entity Type
Business
Contact Information for Business Card
Dennis Lamb
PRT Holdings, Inc.
48216 Fernhill Lane, Unit B
Castaic, CA 93512
Phone: 555.218.6403
Mobile: 555.731.2954
FAX: 555.731.8162
Email: dlamb@prtholdings.example
Web: www.prtholdings.example
Font styles to use
Other font styles liked:
- Helvetica
Look and feel

```html
<!DOCTYPE html>
<html lang="en">
<head>
<meta charset="utf-8">
<title>PRT Holdings, Inc. — Business Card</title>
<link rel="stylesheet" href="https://fonts.googleapis.com/css2?family=Open+Sans:wght@400;600;700&display=swap">
<style>
  :root {
    --brand-blue: #1aaeea;
    --brand-blue-deep: #0f9fdc;
    --paper-top: #ffffff;
    --paper-bottom: #e4e6e8;
    --ink: #3a3d40;
    --stage: #eef0f2;
    --white: #ffffff;
  }
  * { box-sizing: border-box; margin: 0; padding: 0; }
  html, body {
    width: 1200px;
    height: 894px;
    overflow: hidden;
    background: var(--stage);
    font-family: "Open Sans", Helvetica, Arial, sans-serif;
  }
  .sheet {
    position: relative;
    width: 1200px;
    height: 894px;
  }
  .card {
    position: absolute;
    left: 270px;
    width: 660px;
    height: 377px;
    border-radius: 16px;
    overflow: hidden;
    box-shadow: 0 6px 18px rgba(0,0,0,0.12);
  }
  /* Back side */
  .card--back {
    top: 50px;
    background: linear-gradient(135deg, var(--brand-blue) 0%, var(--brand-blue-deep) 100%);
  }
  .card--back .company-name {
    position: absolute;
    left: 44px;
    top: 40px;
    color: var(--white);
    font-size: 30px;
    font-weight: 700;
  }
  /* Front side */
  .card--front {
    top: 467px;
    background: linear-gradient(160deg, var(--paper-top) 0%, var(--paper-top) 35%, var(--paper-bottom) 100%);
  }
  .card--front .company-name {
    position: absolute;
    left: 40px;
    top: 26px;
    color: var(--brand-blue);
    font-size: 30px;
    font-weight: 700;
  }
  .name-tab {
    position: absolute;
    left: 0;
    top: 88px;
    width: 330px;
    height: 70px;
    padding: 9px 0 0 40px;
    background: var(--brand-blue);
    border-radius: 0 35px 35px 0;
    color: var(--white);
  }
  .name-tab .person-name {
    font-size: 22px;
    font-weight: 700;
    letter-spacing: 0.5px;
    line-height: 1.2;
  }
  .name-tab .person-title {
    font-size: 13px;
    font-weight: 400;
    letter-spacing: 1.5px;
    line-height: 1.4;
  }
  .contact-list {
    position: absolute;
    left: 40px;
    top: 180px;
    list-style: none;
  }
  .contact-item {
    display: flex;
    align-items: flex-start;
    gap: 14px;
    color: var(--ink);
    font-size: 17px;
    line-height: 30px;
    letter-spacing: 0.3px;
  }
  .contact-icon {
    flex: none;
    width: 20px;
    height: 20px;
    margin-top: 5px;
  }
  .contact-text span { display: block; }
  .edge-band {
    position: absolute;
    left: 0;
    right: 0;
    bottom: 0;
    height: 14px;
    background: var(--brand-blue);
  }
</style>
</head>
<body>
<main class="sheet">

  <section class="card card--back" aria-label="Card back">
    <p class="company-name">PRT Holdings, Inc.</p>
  </section>

  <section class="card card--front" aria-label="Card front">
    <p class="company-name">PRT Holdings, Inc.</p>

    <div class="name-tab">
      <p class="person-name">DENNIS LAMB</p>
      <p class="person-title">GENERAL MANAGER</p>
    </div>

    <ul class="contact-list">
      <li class="contact-item">
        <svg class="contact-icon" viewBox="0 0 20 20" aria-hidden="true">
          <circle cx="10" cy="10" r="9" fill="none" stroke="var(--brand-blue)" stroke-width="1.5"/>
          <path d="M6.5 8.5 Q10 5.5 13.5 8.5 L12.5 10 L11 9.2 L9 9.2 L7.5 10 Z M7 11.5 H13 V14 H7 Z" fill="var(--brand-blue)"/>
        </svg>
        <span class="contact-text">(555) 218 6403</span>
      </li>
      <li class="contact-item">
        <svg class="contact-icon" viewBox="0 0 20 20" aria-hidden="true">
          <circle cx="10" cy="10" r="9" fill="none" stroke="var(--brand-blue)" stroke-width="1.5"/>
          <rect x="7.3" y="5" width="5.4" height="10" rx="1" fill="none" stroke="var(--brand-blue)" stroke-width="1.4"/>
          <circle cx="10" cy="13.2" r="0.8" fill="var(--brand-blue)"/>
        </svg>
        <span class="contact-text">(555) 731 2954</span>
      </li>
      <li class="contact-item">
        <svg class="contact-icon" viewBox="0 0 20 20" aria-hidden="true">
          <circle cx="10" cy="10" r="9" fill="none" stroke="var(--brand-blue)" stroke-width="1.5"/>
          <rect x="5.5" y="6.8" width="9" height="6.4" fill="none" stroke="var(--brand-blue)" stroke-width="1.3"/>
          <path d="M5.5 6.8 L10 10.5 L14.5 6.8" fill="none" stroke="var(--brand-blue)" stroke-width="1.3"/>
        </svg>
        <span class="contact-text">INFO@PRTHOLDINGS.EXAMPLE</span>
      </li>
      <li class="contact-item">
        <svg class="contact-icon" viewBox="0 0 20 20" aria-hidden="true">
          <circle cx="10" cy="10" r="9" fill="none" stroke="var(--brand-blue)" stroke-width="1.5"/>
          <circle cx="10" cy="10" r="5" fill="none" stroke="var(--brand-blue)" stroke-width="1.2"/>
          <ellipse cx="10" cy="10" rx="2.2" ry="5" fill="none" stroke="var(--brand-blue)" stroke-width="1.1"/>
          <line x1="5" y1="10" x2="15" y2="10" stroke="var(--brand-blue)" stroke-width="1.1"/>
        </svg>
        <span class="contact-text">WWW.PRTHOLDINGS.EXAMPLE</span>
      </li>
      <li class="contact-item">
        <svg class="contact-icon" viewBox="0 0 20 20" aria-hidden="true">
          <circle cx="10" cy="10" r="9" fill="none" stroke="var(--brand-blue)" stroke-width="1.5"/>
          <path d="M10 15.5 C7.5 12.5 6.6 10.8 6.6 9 A3.4 3.4 0 0 1 13.4 9 C13.4 10.8 12.5 12.5 10 15.5 Z" fill="var(--brand-blue)"/>
          <circle cx="10" cy="9" r="1.3" fill="var(--white)"/>
        </svg>
        <span class="contact-text">
          <span>48216 FERNHILL LANE, UNIT B</span>
          <span>CASTAIC, CA 93512</span>
        </span>
      </li>
    </ul>

    <div class="edge-band"></div>
  </section>

</main>
</body>
</html>
```